Harrowgate Building and Property Services needs a business card design

We need a business card design for our building and property services business. We already have a logo we just need a creative design and layout on a business card. Emphasis on clean, modern, professional.
Our client targets are mainly body corporates, building managers, construction managers.
We are a building services company that lean more to structural repair of buildings, through concrete rectification and carbon fibre strengthening.
We also refurbish facades, rendering, painting etc
We target higher end body corporates in prestigious locations, hence why we'd like our cards to reflect professionalism, strength, efficiency

Target Market(s)

body corporates, building managers, construction managers

Industry/Entity Type

Construction

Contact Information for Business Card

Harrowgate is the main word, with 'Building and Property Services' underneath.
Level 17, 88 Marsh Lane
ELMSWORTH
Melbourne
Vic 3942
T: 9218 5371
Duncan Hensley - Director
dunharrowgate@mailbox-example.net

Requirements
Must have
• Stand out on the back of the card- strong/ bold, company logo
• All of the contact details written above
Should not have
• I'd like the card to stand out, especially on the back. Id like the company logo to be prominent, although feel free to be creative around it. But remain clean and professional

```html
<!DOCTYPE html>
<html lang="en">
<head>
<meta charset="utf-8">
<title>Harrowgate Building and Property Services – Business Card</title>
<link rel="stylesheet" href="https://fonts.googleapis.com/css2?family=Arimo:wght@400;700&display=swap">
<style>
  :root {
    --page-bg: #e9e9ec;
    --card-black: #0d0d0f;
    --card-black-soft: #2a2a2e;
    --blue-light: #2fa6e6;
    --blue-mid: #1479c4;
    --blue-deep: #0c4f93;
    --brand-blue: #3aa3e0;
    --white: #ffffff;
    --divider: #9aa3ad;
  }
  * { box-sizing: border-box; margin: 0; padding: 0; }
  html, body {
    width: 1200px; height: 950px; overflow: hidden;
    background: var(--page-bg);
    font-family: "Arimo", Arial, sans-serif;
  }
  .sheet {
    position: relative; width: 1200px; height: 950px;
    display: flex; flex-direction: column; align-items: center; justify-content: center;
    gap: 50px;
  }
  .card {
    position: relative; width: 700px; height: 400px;
    overflow: hidden; border-radius: 4px;
    box-shadow: 0 10px 28px rgba(0,0,0,.28);
  }

  /* Front */
  .card--front { display: flex; background: var(--card-black); }
  .contact-panel {
    width: 46%; height: 100%;
    background: radial-gradient(ellipse at 45% 35%, var(--blue-light) 0%, var(--blue-mid) 55%, var(--blue-deep) 100%);
    color: var(--white);
    padding: 34px 30px 0 38px;
    border-right: 3px solid var(--divider);
  }
  .contact-name { font-weight: 700; font-size: 25px; letter-spacing: .5px; text-transform: uppercase; }
  .contact-role { font-size: 15px; text-transform: uppercase; margin-top: 2px; }
  .contact-address { font-size: 17px; line-height: 1.22; margin-top: 62px; }
  .contact-lines { list-style: none; margin-top: 4px; font-size: 17px; line-height: 1.35; }
  .contact-lines li { display: flex; align-items: center; gap: 8px; white-space: nowrap; }
  .contact-lines svg { width: 14px; height: 14px; flex: none; fill: var(--white); }
  .contact-lines .email { font-size: 14.5px; }

  .brand-panel {
    flex: 1; height: 100%;
    background: linear-gradient(100deg, var(--card-black) 0%, var(--card-black-soft) 55%, var(--card-black) 100%);
    display: flex; align-items: center; justify-content: center;
  }

  /* Back */
  .card--back {
    background: linear-gradient(100deg, var(--card-black) 0%, var(--card-black) 40%, var(--card-black-soft) 62%, var(--card-black) 85%);
    display: flex; align-items: center; justify-content: center;
  }

  /* Brand name lockup */
  .brand { display: flex; flex-direction: column; align-items: center; color: var(--brand-blue); }
  .brand-mark { width: 44px; height: 44px; background: var(--brand-blue); margin-bottom: 18px; }
  .brand-name { font-size: 40px; font-weight: 400; letter-spacing: 5px; text-transform: uppercase; }
  .brand-tagline { font-size: 11.5px; font-weight: 400; letter-spacing: 1.6px; text-transform: uppercase; margin-top: 4px; }
  .card--back .brand-name { font-size: 48px; letter-spacing: 6px; }
  .card--back .brand-tagline { font-size: 13px; letter-spacing: 2px; }
  .card--back .brand-mark { width: 54px; height: 54px; }
</style>
</head>
<body>
<main class="sheet">

  <section class="card card--front" aria-label="Business card front">
    <div class="contact-panel">
      <h1 class="contact-name">Duncan Hensley</h1>
      <p class="contact-role">Director</p>
      <address class="contact-address" style="font-style:normal">
        Level 17, 88 Marsh Lane<br>
        ELMSWORTH, Melbourne<br>
        Vic 3942
      </address>
      <ul class="contact-lines">
        <li>
          <svg viewBox="0 0 16 16" aria-hidden="true"><path d="M3 2h3l1.5 3.5-2 1.3a8 8 0 0 0 3.7 3.7l1.3-2L14 10v3a1 1 0 0 1-1 1A12 12 0 0 1 2 3a1 1 0 0 1 1-1z"/></svg>
          <span>9218 5371</span>
        </li>
        <li>
          <svg viewBox="0 0 16 16" aria-hidden="true"><path d="M1 3h14v10H1z M2 4l6 5 6-5" fill="none" stroke="#fff" stroke-width="1.4"/></svg>
          <span class="email">dunharrowgate@mailbox-example.net</span>
        </li>
        <li>
          <svg viewBox="0 0 16 16" aria-hidden="true"><circle cx="8" cy="8" r="6.5" fill="none" stroke="#fff" stroke-width="1.4"/><path d="M1.5 8h13M8 1.5c-3 3.5-3 9.5 0 13M8 1.5c3 3.5 3 9.5 0 13" fill="none" stroke="#fff" stroke-width="1.1"/></svg>
          <span>www.harrowgate-example.com</span>
        </li>
      </ul>
    </div>
    <div class="brand-panel">
      <div class="brand">
        <span class="brand-mark" aria-hidden="true"></span>
        <span class="brand-name">Harrowgate</span>
        <span class="brand-tagline">Building and Property Services</span>
      </div>
    </div>
  </section>

  <section class="card card--back" aria-label="Business card back">
    <div class="brand">
      <span class="brand-mark" aria-hidden="true"></span>
      <span class="brand-name">Harrowgate</span>
      <span class="brand-tagline">Building and Property Services</span>
    </div>
  </section>

</main>
</body>
</html>
```